Harbor Summit Flyer

We need a company flyer to present our company. Target group: Senior managers of hospitals / care facilities.
Please use the new text from the document "Kongressflyer.pptx".
Design: The last flyer can be used as a design basis - attached here: "Blue Lantern Flyer High Res Compressed.pdf". Please note the layout of the business card. The flyer must visually match the business card.
Logos for the references attached (KTV, Pelmora, Wendlach, Tarnford, Am Blauen Tor, Brunnwerk, Voli, KMBT).
Format: DIN A long in portrait format, front and back printed (or open to alternative suggestions if the format does not appear optimal from a design point of view)
Timing: We need the flyer as soon as possible

```html
<!DOCTYPE html>
<html lang="de">
<head>
<meta charset="utf-8">
<title>Harbor Summit Flyer</title>
<link href="https://fonts.googleapis.com/css2?family=Nunito+Sans:wght@400;600;700&display=swap" rel="stylesheet">
<style>
  :root{
    --stage:#7a7a7a;
    --paper:#ffffff;
    --teal:#0f8a8c;
    --navy:#1b3d5a;
    --blue:#2a7dc4;
    --green:#13918f;
    --text:#3c3c3c;
    --muted:#9a9a9a;
  }
  *{box-sizing:border-box;margin:0;padding:0}
  html,body{width:1200px;height:849px;overflow:hidden;background:var(--stage)}
  body{font-family:"Nunito Sans",Arial,sans-serif;color:var(--text)}
  .flyer{position:absolute;left:350px;top:70px;width:500px;height:708px;background:var(--paper);overflow:hidden;box-shadow:0 6px 18px rgba(0,0,0,.35)}
  .header{position:absolute;left:0;top:0;width:500px;height:81px;background:linear-gradient(105deg,#1c3b58 0%,#1d4f6a 45%,#1c6a74 75%,#2b9a86 100%)}
  .brand-left{position:absolute;left:34px;top:40px;display:flex;align-items:center;gap:6px;color:#fff;font-size:11px;letter-spacing:2.5px;font-weight:400}
  .brand-left .mark{width:8px;height:8px;background:#fff;border-radius:50%}
  .brand-right{position:absolute;right:30px;top:40px;color:#fff;font-size:22px;font-weight:700;letter-spacing:-.5px;line-height:1}
  .brand-right small{display:block;font-size:4px;font-weight:400;letter-spacing:0;text-align:right;margin-top:2px}

  .intro{position:absolute;left:31px;top:96px;width:160px}
  h2{color:var(--blue);font-weight:700;line-height:1.16}
  .intro h2{font-size:12px}
  .rule{width:47px;height:1px;background:var(--muted);margin:9px 0 10px -1px}
  .intro p,.intro li{font-size:8px;line-height:1.6}
  ul{list-style:none}
  .chev li{position:relative;padding-left:15px;margin-bottom:3px}
  .chev li::before{content:"›";position:absolute;left:2px;top:-1px;font-weight:700;color:#333}

  .about{position:absolute;left:199px;top:96px;width:301px;height:154px;background:var(--teal);border-radius:9px 0 0 9px;color:#fff;padding:12px 14px}
  .about h3{font-size:11px;font-weight:600;margin-bottom:11px}
  .about p{font-size:7.7px;line-height:1.63;margin-bottom:7px}

  .why h2{position:absolute;left:30px;top:264px;font-size:11.6px}
  .why-col{position:absolute;top:287px;width:190px;font-size:8px;line-height:1.28}
  .why-col.left{left:30px}
  .why-col.right{left:255px;width:215px}
  .why-divider{position:absolute;left:240px;top:288px;width:1px;height:99px;background:var(--muted)}
  .item{display:flex;gap:6px;margin-bottom:4px}
  .item .ico{flex:0 0 9px;margin-top:1px}
  .item.key{color:var(--green)}
  .item.sub .ico{font-weight:700;text-align:center;color:#333;line-height:1}

  .dots{position:absolute;left:29px;width:442px;border-top:1.3px dotted #b5b5b5}
  .dots.mid{top:402px}

  .positions{position:absolute;left:30px;top:414px;width:222px;height:210px;font-size:8px;line-height:10px}
  .positions > *{position:absolute;left:0;width:100%}
  .positions h2{font-size:11.6px;line-height:14px;top:0}
  .positions .item{margin:0;height:12px;align-items:center}
  .positions .item .ico{margin-top:0}
  .positions .rule{margin:0;width:47px}

  .contacts{position:absolute;left:257px;top:415px;width:213px}
  .contacts h2{font-size:11.6px;margin-bottom:8px}
  .person{position:relative;height:64px;border-bottom:1px solid #a8a8a8}
  .person+.person{margin-top:1px}
  .photo{position:absolute;left:0;top:0;width:55px;height:55px;border-radius:5px;background:linear-gradient(160deg,#d4d4d4,#6d6d6d 65%,#2e2e2e)}
  .person .office{position:absolute;left:61px;color:var(--green);font-size:8.5px;font-weight:600}
  .person .name{position:absolute;left:61px;font-size:6.6px;line-height:1.3;width:82px}
  .person .reach{position:absolute;left:147px;font-size:6.2px;line-height:1.45}

  .refs{position:absolute;left:29px;top:631px;width:442px;display:flex;align-items:center;gap:6px}
  .refs h2{font-size:11.6px;white-space:nowrap}
  .refs .dotline{flex:1;border-top:1.3px dotted #b5b5b5;margin-top:4px}
  .logos{position:absolute;left:29px;top:658px;width:442px;display:flex;justify-content:space-between;align-items:center;font-size:8px;font-weight:700;color:#555}
  .logo{display:flex;align-items:center;gap:3px;white-space:nowrap}
  .logo .sq{width:6px;height:6px;background:#888}
  .logo .ci{width:6px;height:6px;border-radius:50%;background:#888}

  .footer{position:absolute;left:0;bottom:0;width:500px;height:23px;background:var(--teal)}
</style>
</head>
<body>
<main class="flyer">
  <header class="header" role="img" aria-label="Dunkelblau-türkiser Hintergrund mit facettiertem Polygonmuster">
    <div class="brand-left"><span class="mark"></span>BLUE LANTERN</div>
    <div class="brand-right">Veltrand.<small>Beratung im Gesundheitswesen</small></div>
  </header>

  <section class="intro">
    <h2>Sie sind Leiter eines Krankenhauses und suchen...</h2>
    <div class="rule"></div>
    <ul class="chev">
      <li>medizinische Fachkräfte für Ihre Klinik oder</li>
      <li>herausragende Führungskräfte für Ihre Klinikverwaltung?</li>
    </ul>
    <p>Möchten Sie dabei auf Augenhöhe begleitet werden? Wir unterstützen Sie gerne.</p>
  </section>

  <section class="about">
    <h3>Wer sind wir?</h3>
    <p>Seit fast 30 Jahren gehört das Unternehmen Veltrand. / Blue Lantern zu den bedeutensten Personalberatungen im Gesundheitswesen. Die Rekrutierung von Spitzenpersonal für Kliniken ist unsere große Leidenschaft.</p>
    <p>Durch den Zusammenschluss der beiden Firmen haben wir uns im letzten Jahr modernisiert, digitalisiert und für die Zukunft aufgestellt – ohne dabei die Tradition aus den Augen zu verlieren.</p>
  </section>

  <section class="why">
    <h2>Warum können wir Sie bestmöglich unterstützen?</h2>
    <div class="why-col left">
      <div class="item key"><svg class="ico" viewBox="0 0 10 10" width="9" height="9"><rect x="1" y="2" width="7" height="7" fill="none" stroke="#13918f" stroke-width="1.1"/><path d="M2.5 5.3l2 2 4.5-6" fill="none" stroke="#13918f" stroke-width="1.3"/></svg><span>Ehrlichkeit ist uns wichtig ...</span></div>
      <div class="item sub"><span class="ico">›</span><span>bei uns bekommen Sie aufrichtiges Marktfeedback und</span></div>
      <div class="item sub"><span class="ico">›</span><span>garantiert keine Versprechungen, die wir nicht halten können</span></div>
      <div class="item key"><svg class="ico" viewBox="0 0 10 10" width="9" height="9"><rect x="1" y="2" width="7" height="7" fill="none" stroke="#13918f" stroke-width="1.1"/><path d="M2.5 5.3l2 2 4.5-6" fill="none" stroke="#13918f" stroke-width="1.3"/></svg><span>Wir lieben was wir tun ...</span></div>
      <div class="item sub"><span class="ico">›</span><span>und wir arbeiten schnell, effizient und auf Augenhöhe</span></div>
    </div>
    <div class="why-divider"></div>
    <div class="why-col right">
      <div class="item key"><svg class="ico" viewBox="0 0 10 10" width="9" height="9"><rect x="1" y="2" width="7" height="7" fill="none" stroke="#13918f" stroke-width="1.1"/><path d="M2.5 5.3l2 2 4.5-6" fill="none" stroke="#13918f" stroke-width="1.3"/></svg><span>Wir sind Spezialisten im Gesundheitswesen ...</span></div>
      <div class="item sub"><span class="ico">›</span><span>unser Team verfügt über fundiertes Marktverständnis</span></div>
      <div class="item key"><svg class="ico" viewBox="0 0 10 10" width="9" height="9"><rect x="1" y="2" width="7" height="7" fill="none" stroke="#13918f" stroke-width="1.1"/><path d="M2.5 5.3l2 2 4.5-6" fill="none" stroke="#13918f" stroke-width="1.3"/></svg><span>Überragendes Netzwerk ...</span></div>
      <div class="item sub"><span class="ico">›</span><span>in allen Teilsektoren des Gesundheitswesens</span></div>
      <div class="item key"><svg class="ico" viewBox="0 0 10 10" width="9" height="9"><rect x="1" y="2" width="7" height="7" fill="none" stroke="#13918f" stroke-width="1.1"/><path d="M2.5 5.3l2 2 4.5-6" fill="none" stroke="#13918f" stroke-width="1.3"/></svg><span>Digital ...</span></div>
      <div class="item sub"><span class="ico">›</span><span>unsere Prozesse? Transparent! Unsere Suche für Sie 24/7 einsehbar</span></div>
    </div>
  </section>

  <div class="dots mid"></div>

  <section class="positions">
    <h2>Was sind typische Positionen, die wir besetzen?</h2>
    <p style="top:37px">Medizinische Fachkräfte &gt; 100 Besetzungen in vergangenen 2 Jahren in sämtlichen Fachrichtungen, z.B.</p>
    <div class="item" style="top:63px"><svg class="ico" viewBox="0 0 10 10" width="9" height="9"><rect x="1" y="2" width="7" height="7" fill="none" stroke="#444" stroke-width="1.1"/><path d="M2.5 5.3l2 2 4.5-6" fill="none" stroke="#444" stroke-width="1.3"/></svg><span>Chefarzt Gynäkologie / Geburtshilfe</span></div>
    <div class="item" style="top:76px"><svg class="ico" viewBox="0 0 10 10" width="9" height="9"><rect x="1" y="2" width="7" height="7" fill="none" stroke="#444" stroke-width="1.1"/><path d="M2.5 5.3l2 2 4.5-6" fill="none" stroke="#444" stroke-width="1.3"/></svg><span>Chefarzt Radiologie</span></div>
    <div class="item" style="top:89px"><svg class="ico" viewBox="0 0 10 10" width="9" height="9"><rect x="1" y="2" width="7" height="7" fill="none" stroke="#444" stroke-width="1.1"/><path d="M2.5 5.3l2 2 4.5-6" fill="none" stroke="#444" stroke-width="1.3"/></svg><span>Chefarzt Psychiatrie</span></div>
    <div class="rule" style="top:111px"></div>
    <p style="top:118px">Herausragende Führungskräfte &gt; 150 Besetzungen von Leitungspositionen in sämtlichen Geschäftsbereichen in vergangenen 2 Jahren, z.B.</p>
    <div class="item" style="top:154px"><svg class="ico" viewBox="0 0 10 10" width="9" height="9"><rect x="1" y="2" width="7" height="7" fill="none" stroke="#444" stroke-width="1.1"/><path d="M2.5 5.3l2 2 4.5-6" fill="none" stroke="#444" stroke-width="1.3"/></svg><span>Klinik Geschäftsführung / Vorstände</span></div>
    <div class="item" style="top:167px"><svg class="ico" viewBox="0 0 10 10" width="9" height="9"><rect x="1" y="2" width="7" height="7" fill="none" stroke="#444" stroke-width="1.1"/><path d="M2.5 5.3l2 2 4.5-6" fill="none" stroke="#444" stroke-width="1.3"/></svg><span>Leitung Personal</span></div>
    <div class="item" style="top:180px"><svg class="ico" viewBox="0 0 10 10" width="9" height="9"><rect x="1" y="2" width="7" height="7" fill="none" stroke="#444" stroke-width="1.1"/><path d="M2.5 5.3l2 2 4.5-6" fill="none" stroke="#444" stroke-width="1.3"/></svg><span>Leitung Qualitäts- und Risikomanagement</span></div>
    <div class="item" style="top:193px"><svg class="ico" viewBox="0 0 10 10" width="9" height="9"><rect x="1" y="2" width="7" height="7" fill="none" stroke="#444" stroke-width="1.1"/><path d="M2.5 5.3l2 2 4.5-6" fill="none" stroke="#444" stroke-width="1.3"/></svg><span>Leitung Patientenmanagement</span></div>
  </section>

  <section class="contacts">
    <h2>Wir freuen uns, von Ihnen zu hören!</h2>
    <div class="person">
      <div class="photo" role="img" aria-label="Schwarzweiß-Porträtfoto der Ansprechpartnerin in Hamburg"></div>
      <div class="office" style="top:19px">Büro Hamburg</div>
      <div class="name" style="top:33px">Dr. med. Clara Hoven Brandt</div>
      <div class="reach" style="top:32px">chb@bluelantern.io<br>T: +49 170 5521804</div>
    </div>
    <div class="person">
      <div class="photo" role="img" aria-label="Schwarzweiß-Porträtfoto der Ansprechpartnerin in Wien" style="top:4px"></div>
      <div class="office" style="top:24px">Büro Wien</div>
      <div class="name" style="top:38px">Lena Aumayr</div>
      <div class="reach" style="top:29px">la@bluelantern.io<br>T: +43 660 3927150</div>
    </div>
    <div class="person" style="border-bottom:none">
      <div class="photo" role="img" aria-label="Farbiges Porträtfoto der Ansprechpartnerin in Wien" style="top:4px;background:linear-gradient(160deg,#f0f0f0,#c9b4a4 55%,#2a2f3a)"></div>
      <div class="office" style="top:26px">Büro Wien</div>
      <div class="name" style="top:40px">Marit Sonnfeld</div>
      <div class="reach" style="top:31px">ms@bluelantern.io<br>T: +43 660 3927150</div>
    </div>
  </section>

  <div class="refs"><h2>Referenzen</h2><span class="dotline"></span></div>
  <div class="logos">
    <span class="logo">KTV</span>
    <span class="logo">Pelmora</span>
    <span class="logo"><span class="sq"></span>Klinikum Wendlach</span>
    <span class="logo">Am Blauen Tor</span>
    <span class="logo">Brunnwerk</span>
    <span class="logo"><span class="ci"></span>Voli</span>
    <span class="logo">KMBT</span>
  </div>

  <footer class="footer"></footer>
</main>
</body>
</html>
```